Business card and company stationary - Corvane Cleaning Ltd

1. Who are we and who are our customers?

o We are a relatively new cleaning company, established December 2008. We are a small company. We have 24 staff and we offer domestic and commercial cleaning services.
o We both (me and my wife) have been working for many years in the cleaning industry. We worked for some of the biggest and best cleaning companies in UK. We’ve been operatives, supervisors and managers.
o Inevitably after so many years of working for someone else, we decided to start our own business.
o Our domestic customers are middle class families and busy professionals. We’ve got some commercial customers, mainly offices.
o We are growing steadily.

2. What do we do? What are our services?

o Cleaning. We’ve got range of services - not to many but still can be daunting and confusing for some.
o Generally we’ve got domestic and commercial clients. The approach to the domestic cleaning customers is different to the commercial. In the way we want to say that it is cleaning that we do, but we acknowledge the environment and we appreciate the personal circumstances and requirements that are present. We do care, we listen and we try to work out the best possible way to complete our work.
o Mainly we get our work through referrals

3. What do we want with our stationery ?

o To place and maintain our message and reach out to people and organisations
o We want to advertise, communicate and sale.
o We are going to sell services.
o Increase membership, loyalty and support.

We are after business card design, headed letter and compliment slip.
We would like the headed letter to be created in formats suitable for :
- printing format
- also for use in our daily correspondence via e mail with clients and staff in a easy to edit and write format

The website we have is still under contraction and the domain is corvanecleaning.example

Target Market(s)

Families, individuals, businesses.

Industry/Entity Type

Cleaning Service

Contact Information for Business Card

FRONT :
Company Name - Corvane Cleaning Ltd
Company address - 41 Pelbury Rd, Pelbury, Essex, RM14 7QT
Name - Mrs. Teodora Vasilkova - Tedi
Title - Managing Director
Company phone - 020 8837 2591
E mail - tedi.vasilkova@corvanecleaning.example

BACK :

Company website - corvanecleaning.example
E mail - enquiries@corvanecleaning.example

Font styles to use
Serif

Requirements
Must have
• The above items and company logo...maybe at the back. But I'm free for any suggestions.

```html
<!DOCTYPE html>
<html lang="en">
<head>
<meta charset="utf-8">
<title>Corvane Cleaning Ltd – Stationery</title>
<link rel="stylesheet" href="https://fonts.googleapis.com/css2?family=Didact+Gothic&family=Arimo:wght@400;700&display=swap">
<style>
  :root {
    --bg: #e3e3e3;
    --paper: #ffffff;
    --sky: #4fc3f0;
    --sky-faint: #e3f4fb;
    --ink: #1b1b1b;
    --navy: #1d2a3a;
    --brand: #2a7398;
    --label: #3a3a3a;
    --shadow: 4px 5px 6px rgba(0,0,0,.45);
  }
  * { box-sizing: border-box; margin: 0; padding: 0; }
  html, body { width: 1200px; height: 1000px; overflow: hidden; }
  body { background: var(--bg); position: relative; font-family: "Didact Gothic", sans-serif; color: var(--ink); }

  .sheet { position: absolute; background: var(--paper); box-shadow: var(--shadow); overflow: hidden; }

  /* brand block */
  .brand { position: absolute; display: flex; flex-direction: column; align-items: center; }
  .brand__dot { width: 22px; height: 22px; border-radius: 50%; background: var(--navy); margin-bottom: 4px; }
  .brand__name { font-family: "Didact Gothic", sans-serif; color: var(--brand); font-size: 8px; line-height: 1.1; text-align: center; letter-spacing: .3px; }

  .watermark { position: absolute; border-radius: 50%; border: 6px solid var(--sky-faint); }

  /* business cards */
  .card { top: 137px; width: 287px; height: 161px; border-radius: 12px; }
  .card--front { left: 195px; }
  .card--back { left: 510px; background: var(--sky); }
  .card__label { position: absolute; top: 316px; font-size: 8px; letter-spacing: 2px; color: var(--label); }

  .person { position: absolute; left: 27px; top: 85px; }
  .person__name { font-size: 8px; }
  .person__title { font-family: "Arimo", sans-serif; font-weight: 700; font-size: 5.5px; margin-top: 2px; }

  .contacts { position: absolute; list-style: none; }
  .contacts li { display: flex; align-items: center; font-size: 5.8px; height: 7px; }
  .contacts li::before { content: ""; width: 4.5px; height: 4.5px; border-radius: 50%; background: var(--sky); margin-right: 5px; flex: none; }

  .seal { position: absolute; border-radius: 50%; border: 5px solid #fff; display: flex; align-items: center; justify-content: center; text-align: center; color: #fff; }
  .seal__name { font-size: 13px; line-height: 1.25; letter-spacing: .5px; }

  /* envelopes */
  .envelope { left: 170px; width: 443px; }
  .envelope--front { top: 510px; height: 188px; }
  .envelope--back { top: 718px; height: 191px; }
  .envelope__stamp { position: absolute; left: 375px; top: 14px; width: 52px; height: 56px; border: 1.5px solid #d8d8d8; }
  .envelope__window { position: absolute; left: 42px; top: 109px; width: 209px; height: 51px; border: 1px dashed #bdbdbd; border-radius: 6px; }
  .envelope__return { position: absolute; left: 40px; top: 87px; font-size: 5px; line-height: 1.15; }
  .envelope__flap { position: absolute; left: 0; top: 0; }

  /* letterhead */
  .letter { left: 696px; top: 362px; width: 388px; height: 547px; }
  .letter__body { position: absolute; left: 37px; top: 133px; width: 330px; font-family: "Arimo", sans-serif; font-weight: 700; font-size: 4.7px; line-height: 6.3px; }
  .letter__body p { margin-bottom: 5px; }
  .letter__body .gap { margin-bottom: 8px; }
  .signature { position: absolute; left: 9px; top: 390px; width: 112px; height: 56px; background: linear-gradient(90deg, rgba(0,0,0,.06), rgba(0,0,0,0)); border-radius: 6px; }
</style>
</head>
<body>

  <!-- Business card: front -->
  <section class="sheet card card--front">
    <div class="brand" style="left:22px; top:13px; width:60px;">
      <span class="brand__dot"></span>
      <span class="brand__name">Corvane<br>Cleaning Ltd</span>
    </div>
    <div class="person">
      <p class="person__name">John Doe</p>
      <p class="person__title">Managing Director</p>
    </div>
    <ul class="contacts" style="left:27px; top:112px;">
      <li>123-456-7890</li>
      <li>456-123-7890</li>
      <li>john_doe@corvanecleaning.example</li>
      <li>www.corvanecleaning.example</li>
    </ul>
    <span class="watermark" style="left:190px; top:75px; width:100px; height:100px;"></span>
  </section>
  <span class="card__label" style="left:338px;">FRONT</span>

  <!-- Business card: back -->
  <section class="sheet card card--back">
    <div class="seal" style="left:77px; top:14px; width:133px; height:133px;">
      <span class="seal__name">Corvane<br>Cleaning Ltd</span>
    </div>
  </section>
  <span class="card__label" style="left:644px;">BACK</span>

  <!-- Envelope: front -->
  <section class="sheet envelope envelope--front">
    <div class="brand" style="left:50px; top:30px; width:60px;">
      <span class="brand__dot"></span>
      <span class="brand__name">Corvane<br>Cleaning Ltd</span>
    </div>
    <p class="envelope__return">john_doe@corvanecleaning.example<br>www.corvanecleaning.example</p>
    <span class="envelope__stamp"></span>
    <span class="envelope__window"></span>
    <span class="watermark" style="left:320px; top:75px; width:150px; height:150px;"></span>
  </section>

  <!-- Envelope: back -->
  <section class="sheet envelope envelope--back">
    <svg class="envelope__flap" width="443" height="80" viewBox="0 0 443 80">
      <path d="M0 0 H443 V6 Q438 18 420 24 L240 68 Q222 73 204 68 L24 24 Q6 18 0 6 Z" fill="var(--sky)"/>
    </svg>
    <div class="seal" style="left:196px; top:10px; width:50px; height:50px; border-width:2.5px;">
      <span class="seal__name" style="font-size:6px;">Corvane<br>Cleaning Ltd</span>
    </div>
  </section>

  <!-- Letterhead -->
  <section class="sheet letter">
    <div class="brand" style="left:37px; top:28px; width:60px;">
      <span class="brand__dot"></span>
      <span class="brand__name">Corvane<br>Cleaning Ltd</span>
    </div>
    <ul class="contacts" style="left:242px; top:42px; line-height:1;">
      <li style="height:10px;">123-456-7890</li>
      <li style="height:10px;">456-123-7890</li>
      <li style="height:10px;">john_doe@corvanecleaning.example</li>
      <li style="height:10px;">www.corvanecleaning.example</li>
    </ul>

    <div class="letter__body">
      <p class="gap">Duis aute irure dolor in<br>Duis aute irure dolor in</p>
      <p class="gap">Duis aute irure dolor in<br>01632 960418</p>
      <p>Duis aute ,</p>
      <p class="gap">Lorem ipsum dolor sit amet, consectetur adipisicing elit, sed do eiusmod tempor incididunt ut labore et dolore magna aliqua. Ut enim ad minim veniam, quis nostrud exercitation ullamco laboris nisi ut aliquip ex ea commodo consequat. Duis aute irure dolor in reprehenderit in voluptate velit esse cillum dolore eu fugiat nulla pariatur. Excepteur sint occaecat cupidatat non proident, sunt in culpa qui officia deserunt mollit anim id est laborum. Lorem ipsum dolor sit amet, consectetur adipisicing elit, sed do eiusmod tempor incididunt ut labore et dolore magna aliqua. Ut enim ad minim veniam, quis nostrud exercitation ullamco laboris nisi ut aliquip ex ea commodo consequat. Duis aute irure dolor in reprehenderit in voluptate velit esse cillum dolore eu fugiat nulla pariatur. Excepteur sint occaecat cupidatat non proident, sunt in culpa qui officia deserunt mollit anim id est laborum.</p>
      <p class="gap">Lorem ipsum dolor sit amet, consectetur adipisicing elit, sed do eiusmod tempor incididunt ut labore et dolore magna aliqua. Ut enim ad minim veniam, quis nostrud exercitation ullamco laboris nisi ut aliquip ex ea commodo consequat. Duis aute irure dolor in reprehenderit in voluptate velit esse cillum dolore eu fugiat nulla pariatur. Excepteur sint occaecat cupidatat non proident, sunt in culpa qui officia deserunt mollit anim id est laborum.</p>
      <p class="gap">Lorem ipsum dolor sit amet, consectetur adipisicing elit, sed do eiusmod tempor incididunt ut labore et dolore magna aliqua. Ut enim ad minim veniam, quis nostrud exercitation ullamco laboris nisi ut aliquip ex ea commodo consequat. Duis aute irure dolor in reprehenderit in voluptate velit esse cillum dolore eu fugiat nulla pariatur. Excepteur sint occaecat cupidatat non proident, sunt in culpa qui officia deserunt mollit anim id est laborum. Lorem ipsum dolor sit amet, consectetur adipisicing elit, sed do eiusmod tempor incididunt ut labore et dolore magna aliqua.</p>
      <p class="gap">Lorem ipsum dolor sit amet, consectetur adipisicing elit, sed do eiusmod tempor incididunt ut labore et dolore magna aliqua. Ut enim ad minim veniam, quis nostrud exercitation ullamco laboris nisi ut aliquip ex ea commodo consequat. Duis aute irure dolor in reprehenderit in voluptate velit esse cillum dolore eu fugiat nulla pariatur. Excepteur sint occaecat cupidatat non proident, sunt in culpa qui officia deserunt mollit anim id est laborum.</p>
      <p class="gap">consequat. Duis aute irure dolor in reprehenderit in voluptate velit esse cillum dolore eu fugiat nulla pariatur. Excepteur sint occaecat cupidatat non proident.</p>
      <p style="margin-bottom:26px;">Duis aute irure dolor</p>
      <p>Duis aute irure dolor<br><span style="font-weight:400;">irure dolor</span></p>
    </div>
    <div class="signature" role="img" aria-label="Handwritten signature of the sender"></div>
    <span class="watermark" style="left:222px; top:385px; width:200px; height:200px; border-width:8px;"></span>
  </section>

</body>
</html>
```